Reputable business cards for Diplom Kauffrau, Privat und Geschäftslich

The business cards should be reputable, valuable and elegant in order to be able to use them for business. The design should also include a sophistication that is conspicuous. This could be a picture, an ornament, a sublime print or a kind of logo of the initials of my name "MD". The font should be clear and legible.
Target Market(s)
Business contacts, friends and acquaintances
Contact Information for Business Card
Diplom-Kauffrau Mirela Donat
Lindenhofweg 7 50931 Kerpen
Mobil +49 171 804 29 57
e-mail mirela.donat@postwerk.de
Colors
Designer to choose colors to be used in the design.
Requirements
Must have
- Clear and easy to read font My name in larger font than the other information Visual conspicuity / specificity
Nice to have
- Different colors
Should not have
- Ornate font, playful

```html
<!DOCTYPE html>
<html lang="de">
<head>
<meta charset="utf-8">
<title>Mirela Donat – Visitenkarten</title>
<link rel="stylesheet" href="https://fonts.googleapis.com/css2?family=Work+Sans:wght@400;500;600&display=swap">
<style>
  :root {
    --bg: #1c1c1d;
    --card: #2a2a2b;
    --card-edge: #323233;
    --blue: #1a7fd0;
    --white: #f4f4f4;
    --text: #e6e6e6;
  }
  * { margin: 0; padding: 0; box-sizing: border-box; }
  html, body { width: 1200px; height: 900px; overflow: hidden; }
  body {
    background: var(--bg);
    font-family: "Work Sans", Arial, sans-serif;
    position: relative;
  }
  .card {
    position: absolute;
    left: 290px;
    width: 620px;
    height: 354px;
    background: linear-gradient(135deg, var(--card) 0%, var(--card-edge) 60%, var(--card) 100%);
    border-bottom: 4px solid var(--blue);
    box-shadow: 0 18px 40px rgba(0,0,0,0.55);
  }
  .card--front { top: 60px; }
  .card--back { top: 466px; }

  .brand {
    display: flex;
    align-items: center;
    gap: 16px;
  }
  .brand__square {
    width: 44px;
    height: 44px;
    border-radius: 8px;
    background: var(--blue);
    flex: none;
  }
  .brand__name {
    color: var(--white);
    font-weight: 600;
    font-size: 34px;
    letter-spacing: 0.06em;
    text-transform: uppercase;
    white-space: nowrap;
  }
  .card--front .brand {
    position: absolute;
    left: 50%;
    top: 50%;
    transform: translate(-50%, -50%);
  }

  .card--back .brand {
    position: absolute;
    left: 36px;
    top: 150px;
  }
  .card--back .brand__name { font-size: 27px; }
  .card--back .brand__square { width: 36px; height: 36px; border-radius: 7px; }

  .divider {
    position: absolute;
    left: 332px;
    top: 78px;
    width: 2px;
    height: 186px;
    background: var(--blue);
  }

  .contact {
    position: absolute;
    left: 360px;
    top: 82px;
    color: var(--text);
    font-size: 16px;
    line-height: 1.35;
    letter-spacing: 0.04em;
  }
  .contact__name {
    color: var(--blue);
    font-weight: 500;
    font-size: 23px;
    letter-spacing: 0.05em;
    text-transform: uppercase;
    line-height: 1.1;
  }
  .contact__title { margin-bottom: 14px; }
  .contact__address { margin-bottom: 14px; }
  .contact__line { display: flex; align-items: center; gap: 8px; }
  .contact__line svg { width: 13px; height: 13px; flex: none; }
</style>
</head>
<body>
  <section class="card card--front">
    <div class="brand">
      <span class="brand__square"></span>
      <span class="brand__name">Mirela Donat</span>
    </div>
  </section>

  <section class="card card--back">
    <div class="brand">
      <span class="brand__square"></span>
      <span class="brand__name">Mirela Donat</span>
    </div>
    <div class="divider"></div>
    <div class="contact">
      <p class="contact__name">Mirela Donat</p>
      <p class="contact__title">Diplom-Kauffrau</p>
      <p class="contact__address">Lindenhofweg 7<br>50931 Kerpen</p>
      <p class="contact__line">
        <svg viewBox="0 0 16 16" aria-hidden="true"><path d="M4 1.5l2.2 3-1.3 1.6c.8 2 2.3 3.5 4.3 4.3l1.6-1.3 3 2.2-1.3 2.6C7.2 13.6 2.4 8.8 1.4 3.5z" fill="var(--blue)"/></svg>
        +49 171 804 29 57
      </p>
      <p class="contact__line">
        <svg viewBox="0 0 16 16" aria-hidden="true"><rect x="1.5" y="3.5" width="13" height="9" fill="none" stroke="var(--blue)" stroke-width="1.4"/><path d="M1.5 3.5L8 9l6.5-5.5" fill="none" stroke="var(--blue)" stroke-width="1.4"/></svg>
        mirela.donat@postwerk.de
      </p>
    </div>
  </section>
</body>
</html>
```